I already have a logo created by Quillory Makers that I'm very happy with. I need to spruce up my business card now. Its a double sided card with not much info on it, I like to keep it simple.
Front of card: name, phone # email address, web address. Tag Line "Outsourced Technology Solutions", under that it says Business Voice Services & Electronic Protection.
Rear of Card: Content written inside a "cloud" saying "Cloud Solutions" "Cloud Integrity"

Target Market(s)

Business to Business

Industry/Entity Type

Business

Contact Information for Business Card

We are in the technology field. Providing Telephone systems (hardware), SIP Trunks (dial tone/local/long distance/telephone #'s), LAN (Local Area Network)infrastructure cabling, Data Center solutions and Security Applications (Camera systems, Access Control systems,

Requirements
Must have
• Must have brevity
Should not have
• Clutter and/or too much information

```html
<!DOCTYPE html>
<html lang="en">
<head>
<meta charset="utf-8">
<title>Meridian Relay Networks – Business Card</title>
<link rel="stylesheet" href="https://fonts.googleapis.com/css2?family=Open+Sans:wght@400;600;700&family=Raleway:wght@400&family=Roboto:wght@400&display=swap">
<style>
  :root {
    --navy: #0c3d74;
    --navy-deep: #0a3466;
    --paper: #f4f5f6;
    --backdrop: #e4e4e4;
    --ink: #2b2b2b;
    --muted: #5e5e5e;
    --rule: #9aa0a6;
    --band-edge: #6b6f73;
    --white: #ffffff;
  }
  * { margin: 0; padding: 0; box-sizing: border-box; }
  html, body {
    width: 1200px;
    height: 576px;
    overflow: hidden;
    background: var(--backdrop);
  }
  .canvas {
    position: relative;
    width: 1200px;
    height: 576px;
  }
  .card {
    position: absolute;
    top: 138px;
    width: 484px;
    height: 294px;
  }
  /* Rear side */
  .card-rear {
    left: 81px;
    background: linear-gradient(180deg, var(--navy) 0%, var(--navy-deep) 100%);
    display: flex;
    align-items: center;
    justify-content: center;
  }
  .rear-brand {
    display: flex;
    align-items: center;
    gap: 12px;
    font-family: "Open Sans", sans-serif;
    font-weight: 600;
    font-size: 22px;
    line-height: 1.2;
    color: var(--white);
    text-align: left;
  }
  .rear-brand .mark-dot {
    width: 14px;
    height: 14px;
    border-radius: 50%;
    background: var(--white);
    flex: none;
  }
  /* Front side */
  .card-front {
    left: 602px;
    background: var(--paper);
    overflow: hidden;
  }
  .side-band {
    position: absolute;
    left: 0; top: 0;
    width: 42px;
    height: 100%;
    background: var(--navy);
    border-right: 4px solid var(--band-edge);
  }
  .brand-block {
    position: absolute;
    right: 28px;
    top: 26px;
    text-align: right;
  }
  .brand-name {
    display: flex;
    align-items: center;
    justify-content: flex-end;
    gap: 8px;
    font-family: "Open Sans", sans-serif;
    font-weight: 600;
    font-size: 17px;
    line-height: 1.1;
    color: var(--navy);
    padding-bottom: 6px;
    border-bottom: 1px solid var(--rule);
  }
  .brand-name .mark-dot {
    width: 10px;
    height: 10px;
    border-radius: 50%;
    background: var(--navy);
    flex: none;
  }
  .tagline {
    font-family: "Raleway", sans-serif;
    font-size: 12px;
    color: var(--muted);
    margin-top: 4px;
  }
  .person {
    position: absolute;
    left: 64px;
    top: 168px;
  }
  .person-name {
    font-family: "Open Sans", sans-serif;
    font-weight: 700;
    font-size: 21px;
    line-height: 1.1;
    color: var(--navy);
  }
  .person-title {
    font-family: "Roboto", sans-serif;
    font-size: 11.5px;
    color: var(--ink);
    margin-top: 2px;
  }
  .contact-list {
    list-style: none;
    position: absolute;
    left: 64px;
    top: 221px;
    font-family: "Roboto", sans-serif;
    font-size: 12px;
    color: var(--ink);
  }
  .contact-list li {
    display: flex;
    align-items: center;
    gap: 9px;
    height: 18px;
  }
  .contact-list svg {
    width: 10px;
    height: 10px;
    fill: var(--navy);
    flex: none;
  }
</style>
</head>
<body>
<main class="canvas">
  <section class="card card-rear" aria-label="Card rear">
    <div class="rear-brand">
      <span class="mark-dot"></span>
      <span>Meridian Relay<br>Networks, LLC</span>
    </div>
  </section>

  <section class="card card-front" aria-label="Card front">
    <div class="side-band"></div>

    <div class="brand-block">
      <div class="brand-name"><span class="mark-dot"></span><span>Meridian Relay Networks, LLC</span></div>
      <p class="tagline">Outsourced Technology Solutions</p>
    </div>

    <div class="person">
      <h1 class="person-name">Aaron Whitlow</h1>
      <p class="person-title">Managing Director</p>
    </div>

    <ul class="contact-list">
      <li>
        <svg viewBox="0 0 10 10" aria-hidden="true"><path d="M1 3.2C1 2 2.5 1.4 5 1.4S9 2 9 3.2V4H7V3.2H3V4H1z M2.2 8.6L3.2 4.6h3.6l1 4z"/></svg>
        <span>+111 222 3333</span>
      </li>
      <li>
        <svg viewBox="0 0 10 10" aria-hidden="true"><circle cx="5" cy="5" r="4.3" fill="none" stroke="#0c3d74" stroke-width="1"/><ellipse cx="5" cy="5" rx="1.8" ry="4.3" fill="none" stroke="#0c3d74" stroke-width="0.9"/><path d="M0.8 5h8.4" stroke="#0c3d74" stroke-width="0.9"/></svg>
        <span>www.yourwebsite.com</span>
      </li>
      <li>
        <svg viewBox="0 0 10 10" aria-hidden="true"><path d="M0.5 2h9v6h-9z"/><path d="M0.8 2.3L5 5.6 9.2 2.3" fill="none" stroke="#f4f5f6" stroke-width="0.9"/></svg>
        <span>yourname@yourwebsite.com</span>
      </li>
    </ul>
  </section>
</main>
</body>
</html>
```